Business Card needed for Drainor, a growing Septic Service company

Drainor, a growing local septic service company in Pennsylvania, needs updated business cards. We'd like the business card to feature our logo and communicate that we provide Septic Pumping, Installations/Repairs, Restroom Rentals, and 24/7 Emergency Service. The business card should be eye-catching, bold, and clean/simple. We have been in business almost 10 years and would like to expand and update our business brand and image.

Target Market(s)

Residential and Commercial, New and Current Homeowners

Industry/Entity Type

Service

Contact Information for Business Card

Contact on the business card should be: Dean Harlow Owner & Operator
Phone: 610-555-0187
Email: service@drainor-example.com
Website: www.drainor-example.com
Address: 812 Millbrook Lane Easton PA 18042

Font styles to use
Sans Serif

Colors

Designer to choose colors to be used in the design.

Requirements
Must have
• Feature logo on both side of business card.
Nice to have
• We envision the contact information on one side and our services listed on the other side. Utilize the green from the symbol in our logo as part of the design, overall design color scheme should be white, grey, black.

```html
<!DOCTYPE html>
<html lang="en">
<head>
<meta charset="utf-8">
<title>Drainor Business Card</title>
<link href="https://fonts.googleapis.com/css2?family=Montserrat:wght@400;500;700;800&display=swap" rel="stylesheet">
<style>
  :root {
    --backdrop: #a9a9a9;
    --paper: #f2f2f0;
    --charcoal: #2f2f2f;
    --ink: #1a1a1a;
    --muted: #6a6a6a;
    --green: #5cb521;
    --light: #e6e6e6;
  }
  * { box-sizing: border-box; margin: 0; padding: 0; }
  html, body { width: 1200px; height: 1050px; overflow: hidden; }
  body {
    background: var(--backdrop);
    font-family: "Montserrat", sans-serif;
    position: relative;
  }
  .card {
    position: absolute;
    border-radius: 4px;
    box-shadow: 0 5px 0 var(--green), 0 18px 30px rgba(0,0,0,0.28);
  }

  /* Front: contact side */
  .card-front {
    left: 70px; top: 175px;
    width: 400px; height: 700px;
    background: var(--paper);
    padding: 70px 56px 60px;
    display: flex; flex-direction: column;
  }
  .brand { display: flex; align-items: center; gap: 14px; }
  .brand-mark { width: 38px; height: 38px; background: var(--green); flex: none; }
  .brand-name {
    font-weight: 800; font-size: 42px; letter-spacing: 2px;
    text-transform: uppercase; color: var(--ink); line-height: 1;
    white-space: nowrap;
  }
  .person { margin-top: 150px; }
  .person-name {
    font-weight: 700; font-size: 30px; color: var(--green);
    text-transform: uppercase; letter-spacing: 1px;
  }
  .person-role { font-size: 21px; color: var(--ink); margin-top: 4px; }
  .divider { width: 60px; height: 2px; background: #9a9a9a; margin: 42px 0 40px; }
  .address { font-size: 18px; line-height: 1.45; color: var(--muted); }
  .contacts { list-style: none; margin-top: 26px; }
  .contacts li {
    display: flex; align-items: center; gap: 10px;
    font-size: 17px; line-height: 1.75; color: var(--muted);
    white-space: nowrap;
  }
  .contacts svg { width: 15px; height: 15px; flex: none; }

  /* Back: services side */
  .card-back {
    left: 530px; top: 335px;
    width: 620px; height: 354px;
    background: var(--charcoal);
    padding: 80px 40px 0;
    display: flex; flex-direction: column; align-items: center;
  }
  .card-back .brand-mark { width: 56px; height: 56px; }
  .card-back .brand { gap: 18px; }
  .card-back .brand-name { color: var(--light); font-size: 72px; letter-spacing: 5px; }
  .services {
    list-style: none; margin-top: 52px;
    display: flex; flex-wrap: wrap; justify-content: center;
    gap: 10px 22px; max-width: 540px;
  }
  .services li {
    display: flex; align-items: center; gap: 8px;
    font-size: 17px; font-weight: 500; color: #f4f4f4;
  }
  .services li::before {
    content: ""; width: 11px; height: 11px; background: var(--green);
  }
  .services .emergency { color: var(--green); font-weight: 700; }
</style>
</head>
<body>

<section class="card card-front" aria-label="Business card, contact side">
  <div class="brand">
    <span class="brand-mark"></span>
    <span class="brand-name">Drainor</span>
  </div>

  <div class="person">
    <p class="person-name">Dean Harlow</p>
    <p class="person-role">Owner &amp; Operator</p>
  </div>

  <div class="divider"></div>

  <p class="address">812 Millbrook Lane<br>Alderwick PA 18990</p>

  <ul class="contacts">
    <li>
      <svg viewBox="0 0 16 16" aria-hidden="true"><path fill="#5cb521" d="M4 1l2.5 3-1.3 1.6c.9 2 2.5 3.6 4.5 4.5L11.3 8.8l3 2.5-1.5 2.9C7 14 2 9 1.8 3.2z"/></svg>
      610-555-0187
    </li>
    <li>
      <svg viewBox="0 0 16 16" aria-hidden="true"><rect x="1" y="3" width="14" height="10" fill="#5cb521"/><path d="M1 3l7 5.5L15 3" fill="none" stroke="#f2f2f0" stroke-width="1.4"/></svg>
      service@drainor-example.com
    </li>
    <li>
      <svg viewBox="0 0 16 16" aria-hidden="true"><g fill="none" stroke="#5cb521" stroke-width="1.3"><circle cx="8" cy="8" r="6.5"/><ellipse cx="8" cy="8" rx="2.8" ry="6.5"/><path d="M1.5 8h13M2.5 4.8h11M2.5 11.2h11"/></g></svg>
      www.drainor-example.com
    </li>
  </ul>
</section>

<section class="card card-back" aria-label="Business card, services side">
  <div class="brand">
    <span class="brand-mark"></span>
    <span class="brand-name">Drainor</span>
  </div>
  <ul class="services">
    <li>Septic Pumping</li>
    <li>Installations/Repairs</li>
    <li>Restroom Rentals</li>
    <li class="emergency">24/7 Emergency Service</li>
  </ul>
</section>

</body>
</html>
```